Website for Cuff-Tastics
Cuff-Tastics
Project: Website for Cuff-Tastics
Website for Cuff-Tastics - Retailers
Creative Brief
Retailers
Cuff-Tastics.com (pending)
The ‘Perfect Little Black Dress’.  You know when you've found it – chic, elegant, stylish and flattering! What’s not perfect is that sexy LBD’s are made for the mythical woman, the woman with toned, smooth, perfect arms. Dieting, exercise, lifting weights, toddlers and groceries and still perfection eludes us. Being a mere mortal means that changes in skin tone and muscle are inevitable. What to do? Stylish, little numbers can leave you feeling too exposed for comfort.  Dresses with sleeves are often matronly and dowdy. After years of heroic home-lab research and clumsy attempts using pantyhose as sleeves, I had a moment of pure inspiration! What women needed were flattering, interchangeable sleeves without costly, permanent dress alterations. Cuff-tastics was born. Cuff-tastics instantly make the perfect sleeveless LBD wearable by real women with real arms. That one perfect LBD is transformed into two, three, four or more little black dresses. You’re ready for a first date, a party, and a special gala event without extra effort or expense. Made from comfortable, breathable stretch fabric, Cuff-tastics are laser-cut, seamless camisoles with an array of flattering sleeve choices including mesh, lace, chiffon, fitted, and flutter three-quarters. They will become a seamless part of your wardrobe, transforming everything you own. It’s no myth that women of all ages can feel vibrant, energized, and youthful-and they can look that way too.  The key is to embrace who we are and use all the tools available to look our best and feel confident.  Cuff-tastics are sure to be an essential component of your wardrobe. We’ve earned the right to “bare” arms but we may choose not to!
Like a clean look with white space. Like prominent images. Dislike busy-ness. THE IMAGES FOR THE WEBSITE THAT WE WANT CAN BE SEEN HERE: http://qx.zp/8kTRwbnL47
black
Blue used in Logo
above header
http://www.plumerido.com/
http://www.trivok.com/
http://www.cardelune.com/
We'll forward a pdf file with content and a suggested layout. We will upgrade to a commerce site within 3 months. THE IMAGES FOR THE WEBSITE THAT WE WANT CAN BE SEEN HERE: http://qx.zp/8kTRwbnL47

```html
<!DOCTYPE html>
<html lang="en">
<head>
<meta charset="utf-8">
<title>Cuff-Tastics</title>
<link href="https://fonts.googleapis.com/css2?family=Arimo:wght@400;700&family=Tinos:ital,wght@0,400;1,400;1,700&display=swap" rel="stylesheet">
<style>
:root{
  --teal:#a3dbd8;
  --teal-deep:#7fc6c2;
  --ink:#1e1e1e;
  --muted:#555;
  --line:#d6d6d6;
  --cream:#fbf4dc;
  --gold:#d9b877;
  --white:#ffffff;
}
*{margin:0;padding:0;box-sizing:border-box}
html,body{width:1200px;height:802px;overflow:hidden}
body{background:var(--teal);font-family:"Arimo",Arial,sans-serif;color:var(--ink);position:relative}
.site-header{position:absolute;left:0;top:0;width:1200px;height:89px;background:linear-gradient(#b4e3e0,var(--teal))}
.brand{position:absolute;left:218px;top:30px;display:flex;align-items:center;gap:10px;font-size:22px;color:var(--ink);text-transform:uppercase;letter-spacing:1px}
.brand-mark{width:26px;height:26px;border-radius:50%;background:var(--ink)}
.search{position:absolute;left:876px;top:18px;width:132px;height:24px;background:var(--white);border:1px solid var(--teal-deep);font-size:12px;color:#999;padding:5px 8px}
.search svg{position:absolute;right:6px;top:5px}
.main-nav{position:absolute;left:400px;top:54px;display:flex;font-size:17px}
.main-nav a{color:var(--white);text-decoration:none;padding:0 14px;border-left:1px solid rgba(255,255,255,.7);line-height:18px}
.main-nav a:first-child{border-left:none;color:var(--ink);text-decoration:underline}
.hero{position:absolute;left:0;top:96px;width:1200px;height:384px;background:linear-gradient(90deg,#f4e6b3 0%,var(--cream) 40%,#f3e4b8 65%,var(--gold) 100%);border-top:4px solid #cfcfcf}
.hero-photo{position:absolute;top:12px;width:120px;height:362px;background:linear-gradient(#6b4a3a,#2a2a2a 35%,#1a1a1a 70%,#c9a889);border-radius:40px 40px 6px 6px}
.hero-photo.left{left:216px}
.hero-photo.right{left:864px}
.hero-copy{position:absolute;left:340px;top:108px;width:520px;text-align:center;font-family:"Tinos","Times New Roman",serif}
.hero-kicker{font-style:italic;font-size:28px;margin-left:-110px}
.hero-title{font-size:48px;line-height:1.1;margin-bottom:14px}
.hero-tagline{font-style:italic;font-weight:700;font-size:25px;line-height:1.3}
.hero-arrow{position:absolute;top:255px;width:24px;height:30px;background:var(--ink);display:flex;align-items:center;justify-content:center}
.hero-arrow.prev{left:0}
.hero-arrow.next{right:0}
.content{position:absolute;left:0;top:480px;width:1200px;height:283px;background:var(--white)}
.column{position:absolute;top:26px}
.column h2{font-size:17px;font-weight:700;margin-bottom:12px}
.look{left:192px;width:252px}
.designer{left:475px;width:250px}
.contact{left:756px;width:300px}
.divider{position:absolute;top:30px;width:1px;height:230px;background:var(--line)}
.thumbs{display:grid;grid-template-columns:122px 122px;gap:6px}
.thumb{height:70px;background:linear-gradient(135deg,#e6e6e6,#8a8a8a 60%,#2b2b2b)}
.feature{width:250px;height:146px;background:linear-gradient(90deg,#b9c2c7,#7f7b78 45%,#2e6e6a 75%,#c8ccce)}
.blurb{font-size:11px;color:var(--muted);line-height:14px;margin-top:14px}
.read-more{display:block;font-size:11px;font-weight:700;color:var(--ink);text-decoration:none;margin-top:2px}
.contact-list{list-style:none;font-size:13px}
.contact-list li{display:flex;align-items:flex-start;gap:10px;min-height:26px}
.contact-list li.strong{font-weight:700}
.contact-list .small{font-size:11px;color:var(--muted);line-height:14px}
.icon{flex:none;width:16px;height:16px;display:flex;align-items:center;justify-content:center}
.social-square{width:16px;height:16px;background:var(--teal-deep)}
.site-footer{position:absolute;left:0;top:763px;width:1200px;height:39px;background:var(--teal);font-size:12px}
.footer-nav{position:absolute;left:192px;top:13px;display:flex}
.footer-nav a{color:var(--ink);text-decoration:none;padding:0 8px;border-left:1px solid var(--ink);line-height:12px}
.footer-nav a:first-child{padding-left:0;border-left:none}
.copyright{position:absolute;right:72px;top:13px}
</style>
</head>
<body>
<header class="site-header">
  <div class="brand"><span class="brand-mark"></span>Cuff-Tastics</div>
  <div class="search">Search
    <svg width="12" height="12" viewBox="0 0 12 12"><circle cx="5" cy="5" r="3.6" fill="none" stroke="#7a7a7a" stroke-width="1.5"/><line x1="7.6" y1="7.6" x2="11" y2="11" stroke="#7a7a7a" stroke-width="1.5"/></svg>
  </div>
  <nav class="main-nav">
    <a href="#">Home</a><a href="#">Products</a><a href="#">Levels</a><a href="#">Ways to wear</a><a href="#">Where to buy</a><a href="#">About us</a><a href="#">Contact Us</a>
  </nav>
</header>

<section class="hero">
  <div class="hero-photo left" role="img" aria-label="Model standing in a black lace-sleeved dress"></div>
  <div class="hero-copy">
    <p class="hero-kicker">The Perfect</p>
    <h1 class="hero-title">Little Black Dress</h1>
    <p class="hero-tagline">You know when you’ve found it – chic, elegant,<br>stylish and flattering!</p>
  </div>
  <div class="hero-photo right" role="img" aria-label="Model in a black dress with sheer sleeves, hand on hip"></div>
  <a class="hero-arrow prev" href="#" aria-label="Previous"><svg width="10" height="12" viewBox="0 0 10 12"><path d="M8 1 2 6l6 5" fill="none" stroke="#fff" stroke-width="2"/></svg></a>
  <a class="hero-arrow next" href="#" aria-label="Next"><svg width="10" height="12" viewBox="0 0 10 12"><path d="M2 1l6 5-6 5" fill="none" stroke="#fff" stroke-width="2"/></svg></a>
</section>

<main class="content">
  <section class="column look">
    <h2>Create your own look</h2>
    <div class="thumbs">
      <div class="thumb" role="img" aria-label="Model wearing lace sleeves"></div>
      <div class="thumb" role="img" aria-label="Model wearing sheer sleeves"></div>
      <div class="thumb" role="img" aria-label="Model wearing mesh sleeves"></div>
      <div class="thumb" role="img" aria-label="Model wearing teal dress with sleeves"></div>
    </div>
    <p class="blurb">Lorem ipsum dolor sit amet, consectetur adipisc ing elit, sed do eiusmod.</p>
    <a class="read-more" href="#">Read More...</a>
  </section>
  <div class="divider" style="left:456px"></div>
  <section class="column designer">
    <h2>Designer</h2>
    <div class="feature" role="img" aria-label="Designer seated in a teal dress with black sleeves"></div>
    <p class="blurb">Lorem ipsum dolor sit amet, consectetur adipisc ing elit, sed do eiusmod.</p>
    <a class="read-more" href="#">Read More...</a>
  </section>
  <div class="divider" style="left:737px"></div>
  <section class="column contact">
    <h2>Contact Us</h2>
    <ul class="contact-list">
      <li class="strong"><span class="icon"><svg width="14" height="14" viewBox="0 0 14 14"><path d="M3 1h3l1 3-2 1.5a8 8 0 0 0 3.5 3.5L10 7l3 1v3a2 2 0 0 1-2 2A10 10 0 0 1 1 3a2 2 0 0 1 2-2z" fill="#4aa9a4"/></svg></span>9175550142</li>
      <li class="strong"><span class="icon"><svg width="16" height="12" viewBox="0 0 16 12"><rect x="0.5" y="0.5" width="15" height="11" fill="#4aa9a4"/><path d="M1 1l7 6 7-6" fill="none" stroke="#fff" stroke-width="1.2"/></svg></span>hello@marenvolt.com</li>
      <li><span class="icon"><svg width="12" height="16" viewBox="0 0 12 16"><path d="M6 0a6 6 0 0 1 6 6c0 4-6 10-6 10S0 10 0 6a6 6 0 0 1 6-6z" fill="#4aa9a4"/><circle cx="6" cy="6" r="2.2" fill="#fff"/></svg></span><span class="small">Lorem ipsum dolor sit amet, consectetur di ing elit, sed do eiusmod.</span></li>
      <li class="small"><span class="icon"><span class="social-square"></span></span>Join us on Friendspace</li>
      <li class="small"><span class="icon"><span class="social-square"></span></span>Follow us on Chirpline</li>
      <li class="small"><span class="icon"><span class="social-square"></span></span>Follow us on Circlenet</li>
    </ul>
  </section>
</main>

<footer class="site-footer">
  <nav class="footer-nav">
    <a href="#">Home</a><a href="#">Products</a><a href="#">Levels</a><a href="#">Ways to wear</a><a href="#">Where to buy</a><a href="#">About us</a><a href="#">Contact Us</a>
  </nav>
  <p class="copyright">Copy Right 2013.</p>
</footer>
</body>
</html>
```